Graphic lion print design with text

I like the gold effects in image 2 as described in my attached document, but i'm open to other suggestions. The desired image is image 1. This is a gift for a Leo friend. This is going to be printed and framed to be hung on the wall in a large frame, in landscape format. I like the idea of using different font styles to separate the statements.

• I’m open to the suggestions about the font styles, but I want to separate the statements by using different font styles as shown in attached document.
Must be landscape format.
Small fonts preferred, as shown in the attached image.
• I like the gold effect in image 2 but other suggestions/colours welcome
• Please don't stretch the picture so I can have a good resolution. Place the text on another black background template and then paste the picture beside to the text.

```html
<!DOCTYPE html>
<html lang="en">
<head>
<meta charset="UTF-8">
<title>For God Is With You – Lion Print</title>
<link href="https://fonts.googleapis.com/css2?family=UnifrakturMaguntia&family=Oswald:wght@600;700&family=Quicksand:wght@500&family=Great+Vibes&family=Dancing+Script:wght@500&family=Playfair+Display:wght@600;700&display=swap" rel="stylesheet">
<style>
  :root {
    --bg: #000000;
    --gold: #d8b43c;
    --gold-deep: #8a6f2a;
    --gold-glow: #c9a346;
  }
  html, body {
    margin: 0;
    padding: 0;
    width: 1200px;
    height: 835px;
    overflow: hidden;
    background: var(--bg);
  }
  .print {
    position: relative;
    width: 1200px;
    height: 835px;
    background: var(--bg);
    color: var(--gold);
    overflow: hidden;
  }
  .lion-art {
    position: absolute;
    left: 620px;
    top: 0;
    width: 580px;
    height: 835px;
  }
  .line {
    position: absolute;
    margin: 0;
    white-space: nowrap;
    line-height: 1;
  }
  .blackletter { font-family: "UnifrakturMaguntia", serif; }
  .bold-sans { font-family: "Oswald", sans-serif; font-weight: 700; }
  .round-sans { font-family: "Quicksand", sans-serif; font-weight: 500; letter-spacing: 0.5px; }
  .script { font-family: "Great Vibes", cursive; }
  .script-narrow { font-family: "Dancing Script", cursive; font-weight: 500; }
  .serif { font-family: "Playfair Display", serif; font-weight: 700; }
  .centered { transform: translateX(-50%); }
</style>
</head>
<body>
<main class="print">
  <svg class="lion-art" viewBox="0 0 580 835" role="img" aria-label="Roaring lion head in profile, rendered in gold, dissolving into scattered gold glitter particles">
    <defs>
      <radialGradient id="lionGlow" cx="0.68" cy="0.5" r="0.6">
        <stop offset="0" stop-color="#a88f4e"/>
        <stop offset="0.45" stop-color="#6e5a2a"/>
        <stop offset="0.8" stop-color="#2a2110"/>
        <stop offset="1" stop-color="#000000"/>
      </radialGradient>
    </defs>
    <rect width="580" height="835" fill="url(#lionGlow)"/>
  </svg>

  <p class="line blackletter centered" style="left:327px; top:60px; font-size:21px;">It doesn’t matter who or what may come against you,</p>
  <p class="line bold-sans centered" style="left:327px; top:91px; font-size:33px;">FOR GOD IS WITH YOU</p>
  <p class="line round-sans centered" style="left:327px; top:133px; font-size:22px;">HE has made you more than a conqueror.</p>

  <p class="line" style="left:58px; top:196px;"><span class="script" style="font-size:54px;">Almighty God</span> <span class="round-sans" style="font-size:22px;">will come through for you</span></p>
  <p class="line" style="left:89px; top:266px;"><span class="script" style="font-size:36px;">when you seek Him</span> <span class="round-sans" style="font-size:22px;">in your moments</span></p>
  <p class="line round-sans" style="left:272px; top:313px; font-size:22px;">of trouble and unrest.</p>

  <p class="line" style="left:67px; top:362px;"><span class="serif" style="font-size:40px; font-weight:600;">May God</span> <span class="script-narrow" style="font-size:26px;">calm the restlessness of your mind</span></p>
  <p class="line" style="left:90px; top:416px;"><span class="script-narrow" style="font-size:26px;">and</span> <span class="serif" style="font-size:25px;">still the thoughts that worry you.</span></p>

  <p class="line" style="left:72px; top:476px;"><span class="bold-sans" style="font-size:40px; font-weight:600;">DOORS</span> <span class="round-sans" style="font-size:25px;">will open for you</span></p>
  <p class="line blackletter" style="left:121px; top:523px; font-size:25px;">in the most unlikeliest of places.</p>

  <p class="line serif" style="left:65px; top:584px; font-size:24px;">When you go through deep waters,</p>
  <p class="line script" style="left:132px; top:616px; font-size:44px;">He will be with you.</p>
  <p class="line serif" style="left:185px; top:663px; font-size:27px;">Never will He leave you,</p>
  <p class="line serif" style="left:90px; top:697px; font-size:27px;">never will He forsake you.</p>

  <p class="line round-sans centered" style="left:288px; top:757px; font-size:32px;">AMEN.</p>
</main>
</body>
</html>
```